Präsentationsmappe für Behandlungspläne (DIN A4)
Zielgruppe
Wir sind eine Zahnarztpraxis und suchen ein hochwertiges Design für eine Dokumentenmappe (DIN A4) für unsere Patienten. Die Patienten bekommen in dieser Mappe alle Behandlungspläne oder weitere Unterlagen mit nach Hause.
Aufgabenstellung
Unsere Praxisfarben sind weiss/grau/türkis siehe Homepage der Praxis www.brunholt-partner.de
In die Mappen sollen später DIN-A4 Papiere eingelegt werden. Die Mappen sollen bei Druckwerkstatt Kessling gedruckt werden. Die Dokumentenübergabe soll später als InDesignDokument und als druckfertigtes PDF für Firma Druckwerkstatt Kessling erfolgen
Firmenlogo und Schriftzüge stehen als Indd-Datei zur Verfügung.

```html
<!DOCTYPE html>
<html lang="de">
<head>
<meta charset="utf-8">
<title>Präsentationsmappe – Dr. Brunholt &amp; Partner</title>
<link rel="stylesheet" href="https://fonts.googleapis.com/css2?family=Jost:wght@300;400;500&family=Oswald:wght@300;700&display=swap">
<style>
  :root {
    --teal: #5bbdbb;
    --teal-light: #a9d8d6;
    --ink: #1a1a1a;
    --grey: #4a4a4a;
    --paper: #ffffff;
    --line: #333333;
  }
  html, body { margin: 0; padding: 0; }
  body {
    width: 848px; height: 1200px; overflow: hidden;
    background: var(--paper); position: relative;
    font-family: "Jost", sans-serif; color: var(--ink);
  }
  .spread {
    position: absolute; left: 99px; width: 521px; height: 360px;
    border: 0.8px solid var(--line); box-sizing: border-box;
  }
  .spread--outside { top: 200px; }
  .spread--inside { top: 636px; }
  .page { position: absolute; top: 0; height: 100%; width: 50%; overflow: hidden; }
  .page--left { left: 0; border-right: 0.8px solid var(--line); box-sizing: border-box; }
  .page--right { right: 0; }

  .cover-field { position: absolute; left: 40px; right: 0; top: 0; bottom: 0; background: var(--teal); }
  .cover-tooth {
    position: absolute; left: 0; top: 45px; width: 83px; height: 213px;
    background: var(--paper); border-radius: 0 40px 40px 20px;
  }
  .cover-title {
    position: absolute; left: 23px; top: 316px; margin: 0;
    color: var(--paper); font-weight: 400; font-size: 14px; line-height: 1; letter-spacing: 0; white-space: nowrap;
  }
  .cover-subtitle {
    position: absolute; left: 23px; top: 335px; margin: 0;
    color: var(--paper); font-weight: 400; font-size: 8.4px; line-height: 1; letter-spacing: 0.5px; white-space: nowrap;
  }

  .inside-tooth {
    position: absolute; left: 111px; top: 166px; width: 150px; height: 194px;
    background: var(--teal-light); border-radius: 40px 0 0 0;
  }

  .letterhead { position: absolute; left: 30px; top: 280px; width: 220px; }
  .letterhead__mark {
    position: absolute; left: 111px; top: -4px; width: 22px; height: 22px;
    border-radius: 50%; background: var(--teal);
  }
  .letterhead__name { position: absolute; left: 0; top: 10px; margin: 0; font-size: 8.2px; font-weight: 400; color: var(--grey); white-space: nowrap; }
  .letterhead__tag { position: absolute; left: 0; top: 21px; margin: 0; font-size: 4.6px; color: var(--teal); letter-spacing: 0.3px; white-space: nowrap; }
  .contact { position: absolute; top: 37px; left: 0; display: flex; font-size: 3.1px; line-height: 5.3px; color: var(--grey); }
  .contact__col { padding: 0 3px; border-left: 0.5px solid var(--teal); white-space: nowrap; }
  .contact__col:first-child { padding-left: 0; border-left: none; }
  .contact__key { color: var(--teal); font-weight: 500; }

  .label-below { position: absolute; top: 565px; margin: 0; font-family: "Oswald", sans-serif; font-weight: 300; font-size: 18px; line-height: 1; }
  .label-below--back { left: 144px; }
  .label-below--front { left: 482px; }
  .label-side {
    position: absolute; margin: 0; font-family: "Oswald", sans-serif; font-weight: 700; font-size: 30px; line-height: 1;
    transform: translate(-50%, -50%) rotate(-90deg); white-space: nowrap;
  }
  .label-side--outside { left: 653px; top: 358px; }
  .label-side--inside { left: 653px; top: 797px; }
</style>
</head>
<body>
  <section class="spread spread--outside" aria-label="Mappe außen">
    <div class="page page--left" aria-label="Rückseite"></div>
    <div class="page page--right" aria-label="Vorderseite">
      <div class="cover-field">
        <div class="cover-tooth" role="img" aria-label="Weiße Zahnform als Aussparung"></div>
        <h1 class="cover-title">DR. BRUNHOLT &amp; PARTNER</h1>
        <p class="cover-subtitle">Praxis für Zahnmedizin und Implantologie</p>
      </div>
    </div>
  </section>
  <p class="label-below label-below--back">hinten</p>
  <p class="label-below label-below--front">vorne</p>
  <p class="label-side label-side--outside">Außen</p>

  <section class="spread spread--inside" aria-label="Mappe innen">
    <div class="page page--left" aria-label="Innenseite links">
      <div class="letterhead">
        <span class="letterhead__mark"></span>
        <p class="letterhead__name">DR. BRUNHOLT &amp; PARTNER</p>
        <p class="letterhead__tag">Praxis für Zahnmedizin und Implantologie</p>
        <div class="contact">
          <div class="contact__col">Praxis<br>Dr. Brunholt &amp; Partner<br>Am Lindenhof 12<br>64521 Wendelau</div>
          <div class="contact__col">Master of Science für<br>Ästhetisch Rekonstruktive Zahnmedizin<br>Gutachter und Spezialist für Prothetik<br>Zertifizierter Implantologe</div>
          <div class="contact__col"><span class="contact__key">T</span> 06342 - 4 18 20<br><span class="contact__key">F</span> 06342 - 418 299<br><span class="contact__key">E</span> kontakt@brunholt-partner.de<br><span class="contact__key">W</span> www.brunholt-partner.de</div>
          <div class="contact__col">Bankverbindung<br>Wendelauer Heilberufebank<br><span class="contact__key">IBAN</span> DE00 1234 5678 9012 3456 78<br><span class="contact__key">BIC</span> WHBKDEWEXXX</div>
        </div>
      </div>
    </div>
    <div class="page page--right" aria-label="Innenseite rechts">
      <div class="inside-tooth" role="img" aria-label="Helltürkise Zahnform als Hintergrundmotiv"></div>
    </div>
  </section>
  <p class="label-side label-side--inside">Innen</p>
</body>
</html>
```